International Wine events organiser seeks simple but stunning business card

I am a freelance events, marketing and PR provider specialised in the Wine industry. I help wineries and wine regions reach trade and consumers in foreign markets through events, help with the websites and communications, press trips and promotional activities. I am looking for a business card which is simple yet effective and is linked to events and communication.

I work mainly - but exclusively - with Italian wineries organising events for them in foreign market.s

I would like to use red in the logo as my present website (lunabrendor.com) used grey and red (although I will be changing the design at a later date).

Target Market(s)

Wine producers, promotional bodies in wine sector, companies looking to hire event organisers,

Industry/Entity Type

Marketing

Requirements
Must have
• My Name - Luna Brendor
My address
My phone
My website : www.lunabrendor.com
my Blog : pebbleandtwig.me

Should not have
• Butterflies, stars, flowers, anything not particularly linked to wine - would like to keep it simple, modern and eye-catching without being too cliche.

```html
<!DOCTYPE html>
<html lang="en">
<head>
<meta charset="utf-8">
<title>Luna Brendor – Business Card</title>
<link rel="stylesheet" href="https://fonts.googleapis.com/css2?family=Jost:wght@300;400&display=swap">
<style>
  :root {
    --backdrop: #acacac;
    --card-white: #ffffff;
    --wine-red: #a8191a;
    --name-brown: #6a2a2c;
    --tagline-rose: #8c4548;
    --contact-rose: #dc9b9b;
    --card-shadow: #8a8aa2;
  }
  html, body {
    margin: 0;
    padding: 0;
    overflow: hidden;
  }
  .canvas {
    position: relative;
    width: 1200px;
    height: 404px;
    background: var(--backdrop);
    font-family: "Jost", sans-serif;
    overflow: hidden;
  }
  .card {
    position: absolute;
    top: 52px;
    width: 478px;
    height: 286px;
    box-shadow: 8px 8px 4px var(--card-shadow);
  }
  .card--front {
    left: 77px;
    background: var(--card-white);
  }
  .card--back {
    left: 645px;
    background: var(--wine-red);
  }
  .brand-mark {
    position: absolute;
    left: 44px;
    top: 150px;
    width: 86px;
    height: 86px;
    background: var(--wine-red);
  }
  .brand-name {
    position: absolute;
    left: 135px;
    top: 164px;
    margin: 0;
    font-weight: 400;
    font-size: 38px;
    line-height: 1;
    letter-spacing: 0.5px;
    color: var(--name-brown);
  }
  .brand-tagline {
    position: absolute;
    left: 136px;
    top: 211px;
    margin: 0;
    font-weight: 300;
    font-size: 18.5px;
    line-height: 26px;
    color: var(--tagline-rose);
  }
  .contact {
    position: absolute;
    left: 37px;
    top: 30px;
    margin: 0;
    font-style: normal;
    font-weight: 300;
    font-size: 18.5px;
    line-height: 24.6px;
    color: var(--contact-rose);
  }
  .contact p {
    margin: 0 0 24.6px;
  }
  .contact p:last-child {
    margin-bottom: 0;
  }
</style>
</head>
<body>
<main class="canvas">
  <section class="card card--front" aria-label="Card front">
    <span class="brand-mark" aria-hidden="true"></span>
    <h1 class="brand-name">LUNA BRENDOR</h1>
    <p class="brand-tagline">Communication and Events<br>for the World of Wine</p>
  </section>

  <section class="card card--back" aria-label="Card back">
    <address class="contact">
      <p>Luna Brendor<br>Kastanienweg, 12<br>80331 Munich</p>
      <p>www.lunabrendor.com<br>pebbleandtwig.me<br>Tel: +49 170 5550 123<br>luna@lunabrendor.com</p>
    </address>
  </section>
</main>
</body>
</html>
```